Venture Capital firm needs modern business cards

We are a Venture Capital firm within financial services/Asset management. The industry generally has basic business cards with black, blue and maybe green/yellow design elements.
Our firm has a four-colour swoosh logo. We are based in London and want to stand out, just a little bit!, from the crowd. Our company is called ROLK Investments and the 'C' stands for collaboration thus using artfolkhub is a natural portal for our business card design competition. Our logo came via artfolkhub too!
We use 'Venture Partner in Asset Management' as our tagline and this is Trademark registered. We operate in a conservative industry and we should not overstep our mark. The logo is colorful as it is and therefore the rest of the design should not be too fanciful.
The objective is twofold: make our logo element stick and memorable with our audience, whilst representing a conservative yet young image.
The Business Card obviously needs a field for Name, Surname, Job Title, Adress fields: Street, City, Postcode, Country, telefone and cell number, website address, etc.
We have uploaded the ai file. We trust that these are OK. If not, please advise.
Reason: We have have been busy with a client engagement. We will set the project as Guaranteed in return for the troubles we cause. Apologies for the confusion.
Thank you all for these great and creative design suggestions. The team is very happy with a number of your ideas! We will be in touch tomorrow to give individual feedback before the project closes on Friday. We look forward to working with some of you to narrow down your creations. Thank you, ROLK Investments team.
All,
Target Market(s)
Financial Services Professionals, Investors, Media, 35-70 years, mainly male, well educated
Industry/Entity Type
Conservative
Requirements
Must have
- We must make use of our logo and potential tagline 'Venture Partner in Asset Management' as we are establishing a new Brand and new company in the market.
We can use 'ROLK', 'ROLK Investments', and 'ROLK Investments'+tagline 'Venture Partner in Asset Management' or simply the four-colour swoosh plus the name of the company as part of the text. (see files)
All design elements are available in black or grey-scale if required. (grey scale swoosh attached).
Due to regulation we must have the following wording on the card in small print 'ROLK Investments is an Appointed Representative of Brambury Monetary Ventures Limited, which is authorised by the Pemberton Oversight Board'.
Nice to have
- We would consider designs that make use of different printing techniques such embossing/debossing, UV spot etc.
We attach our colour palette in the files section for your reference.
Should not have
- The font we use for our company name is 'EXO' so do not use a font style that clashes with the corporate fonts, please.
Do not use other design elements than the ones we provide in the file library as part of this project.

```html
<!DOCTYPE html>
<html lang="en">
<head>
<meta charset="utf-8">
<title>ROLK Investments – Business Card</title>
<link rel="stylesheet" href="https://fonts.googleapis.com/css2?family=Exo+2:wght@400;500&family=Open+Sans:wght@400;600&display=swap">
<style>
  :root {
    --backdrop: #e9e7e3;
    --card-dark: #3a3a3a;
    --card-light: #eeeeee;
    --ink: #3b3b3b;
    --ink-soft: #555555;
    --accent-blue: #7bb8cf;
    --accent-orange: #f0a01c;
    --white: #ffffff;
  }
  * { box-sizing: border-box; margin: 0; padding: 0; }
  html, body { width: 1200px; height: 900px; overflow: hidden; }
  body {
    background: var(--backdrop);
    font-family: "Open Sans", Arial, sans-serif;
    color: var(--ink);
    display: flex;
    align-items: center;
    justify-content: center;
    gap: 60px;
  }
  .card {
    width: 525px;
    height: 300px;
    border-radius: 3px;
    box-shadow: 0 6px 18px rgba(0,0,0,0.12);
    position: relative;
  }

  /* Front */
  .card--front {
    background: var(--card-dark);
    display: flex;
    align-items: center;
    justify-content: center;
    gap: 18px;
  }
  .front-mark {
    width: 54px; height: 54px;
    border-radius: 50%;
    background: var(--accent-orange);
  }
  .front-name {
    font-family: "Exo 2", Arial, sans-serif;
    font-weight: 500;
    font-size: 46px;
    color: var(--white);
    letter-spacing: 1px;
  }

  /* Back */
  .card--back {
    background: var(--card-light);
    padding: 34px 32px 22px 36px;
  }
  .brand {
    position: absolute;
    top: 36px; left: 36px;
    display: flex;
    align-items: center;
    gap: 12px;
  }
  .brand-mark {
    width: 40px; height: 40px;
    border-radius: 50%;
    background: var(--accent-orange);
  }
  .brand-name {
    font-family: "Exo 2", Arial, sans-serif;
    font-weight: 500;
    font-size: 26px;
    color: var(--ink);
  }
  .contact {
    position: absolute;
    top: 36px; right: 32px;
    font-size: 11.5px;
    line-height: 1.45;
    color: var(--ink);
  }
  .contact-row { display: flex; gap: 10px; }
  .contact-label { width: 10px; }
  .address { margin-top: 10px; padding-left: 20px; }
  .person {
    position: absolute;
    top: 132px; left: 90px;
  }
  .person-name {
    font-size: 19px;
    font-weight: 600;
    color: var(--ink);
  }
  .person-title {
    font-size: 14px;
    color: var(--ink-soft);
    margin-top: 2px;
  }
  .website {
    display: inline-block;
    margin-top: 18px;
    font-size: 13px;
    color: var(--ink);
    padding-bottom: 5px;
    border-bottom: 2px solid var(--accent-blue);
  }
  .legal {
    position: absolute;
    left: 90px; right: 32px; bottom: 24px;
    font-size: 8.5px;
    line-height: 1.4;
    color: var(--ink-soft);
  }
</style>
</head>
<body>
  <section class="card card--front" aria-label="Card front">
    <span class="front-mark" aria-hidden="true"></span>
    <span class="front-name">ROLK</span>
  </section>

  <section class="card card--back" aria-label="Card back">
    <div class="brand">
      <span class="brand-mark" aria-hidden="true"></span>
      <span class="brand-name">ROLK Investments</span>
    </div>

    <div class="contact">
      <div class="contact-row"><span class="contact-label">T</span><span>555 014 2280</span></div>
      <div class="contact-row"><span class="contact-label">M</span><span>555 014 2280</span></div>
      <div class="contact-row"><span class="contact-label">E</span><span>edmund@rolk-invest.example</span></div>
      <div class="address">
        Larkmoor 14, Col. Verdant<br>
        Eastvale DF 04821, MX
      </div>
    </div>

    <div class="person">
      <div class="person-name">Edmund Rowe Halvard</div>
      <div class="person-title">Founder &amp; CEO</div>
      <div class="website">www.rolk-invest.example</div>
    </div>

    <p class="legal">ROLK Investments is an Appointed Representative of Brambury Monetary Ventures Limited,<br>which is authorised by the Pemberton Oversight Board</p>
  </section>
</body>
</html>
```